Business Card Design

I'm after a modern and artistic business card design, with clean lines and popping colour. The business card should be professional looking and promote my business.

```html
<!DOCTYPE html>
<html lang="en">
<head>
<meta charset="utf-8">
<title>Mira Petal – Makeup Artist Business Card</title>
<link href="https://fonts.googleapis.com/css2?family=Playfair+Display:ital,wght@0,400;1,400&family=Open+Sans+Condensed:wght@300;700&family=Open+Sans:wght@400;600&display=swap" rel="stylesheet">
<style>
  :root {
    --canvas: #ecebe9;
    --magenta: #c0146e;
    --magenta-deep: #8a0a4c;
    --magenta-light: #e0559a;
    --ink: #1c1c1c;
    --charcoal: #2b2b2b;
    --charcoal-light: #555;
    --white: #ffffff;
    --powder: #f2b7c4;
    --powder-soft: #fbe4ea;
    --grey-text: #eaeaea;
  }
  * { box-sizing: border-box; margin: 0; padding: 0; }
  html, body { width: 1200px; height: 811px; overflow: hidden; }
  body {
    background: var(--canvas);
    font-family: "Open Sans", Arial, sans-serif;
    position: relative;
  }
  .card {
    position: absolute;
    top: 257px;
    width: 520px;
    height: 297px;
    border-radius: 3px;
    overflow: hidden;
    box-shadow: 0 10px 26px rgba(0,0,0,.18);
  }

  /* ---------- Back: photo side + contact panel ---------- */
  .card-back { left: 50px; background: var(--white); }
  .back-visual {
    position: absolute; left: 0; top: 0; width: 330px; height: 297px;
    background: var(--white);
  }
  .powder-photo {
    position: absolute; left: 0; top: 95px; width: 300px; height: 202px;
    background: radial-gradient(ellipse at 45% 45%, var(--powder) 0%, var(--powder-soft) 55%, var(--white) 85%);
  }
  .back-name {
    position: absolute; left: 30px; top: 30px;
    font-family: "Playfair Display", Georgia, serif;
    font-size: 34px; color: var(--magenta); line-height: 1;
  }
  .back-tagline {
    position: absolute; left: 120px; top: 68px;
    font-family: "Playfair Display", Georgia, serif; font-style: italic;
    font-size: 14px; color: var(--ink);
  }
  .back-panel {
    position: absolute; right: 0; top: 0; width: 200px; height: 297px;
    background: linear-gradient(180deg, var(--charcoal-light) 0%, var(--charcoal) 45%, #1a1a1a 100%);
    border-left: 3px solid var(--magenta);
  }
  .brush-photo {
    position: absolute; left: 20px; top: 18px; width: 165px; height: 55px;
    background: linear-gradient(100deg, transparent 0%, #6d6d6d 40%, #b9b9b9 70%, var(--powder) 100%);
    opacity: .55; border-radius: 30px;
  }
  .contact-list {
    position: absolute; left: 18px; bottom: 28px; list-style: none;
    font-family: "Open Sans Condensed", "Arial Narrow", sans-serif; font-weight: 300;
    font-size: 15px; color: var(--grey-text);
  }
  .contact-list li { display: flex; align-items: center; gap: 9px; height: 26px; }
  .contact-list svg { width: 16px; height: 16px; flex: none; }

  /* ---------- Front: magenta card with name band ---------- */
  .card-front {
    left: 630px;
    background: radial-gradient(ellipse at 50% 40%, var(--magenta-light) 0%, var(--magenta) 45%, var(--magenta-deep) 100%);
  }
  .name-band {
    position: absolute; left: 55px; top: 92px; width: 410px; height: 100px;
    background: var(--white);
    box-shadow: 0 4px 14px rgba(0,0,0,.35);
  }
  .name-band::before, .name-band::after {
    content: ""; position: absolute; left: 0; right: 0; height: 4px;
    background: var(--ink); border-bottom: 3px solid var(--magenta);
  }
  .name-band::before { top: 8px; }
  .name-band::after { bottom: 8px; }
  .front-name {
    position: absolute; left: 70px; top: 28px;
    font-family: "Playfair Display", Georgia, serif;
    font-size: 40px; color: var(--magenta); line-height: 1;
  }
  .front-tagline {
    position: absolute; left: 230px; top: 66px;
    font-family: "Playfair Display", Georgia, serif; font-style: italic;
    font-size: 14px; color: var(--ink);
  }
  .front-contact {
    position: absolute; bottom: 18px;
    font-family: "Open Sans Condensed", "Arial Narrow", sans-serif; font-weight: 700;
    font-size: 14px; color: var(--white); letter-spacing: .3px;
  }
  .front-email { left: 22px; }
  .front-phone { left: 230px; }
  .front-web { right: 22px; }
</style>
</head>
<body>

  <section class="card card-back" aria-label="Business card back">
    <div class="back-visual">
      <div class="powder-photo" role="img" aria-label="Photo of loose pink blush powder spilling from a clear jar"></div>
      <div class="back-name">Mira Petal</div>
      <div class="back-tagline">makeup artist</div>
    </div>
    <div class="back-panel">
      <div class="brush-photo" role="img" aria-label="Photo of a makeup brush tipped with pink powder"></div>
      <ul class="contact-list">
        <li>
          <svg viewBox="0 0 16 16" fill="none" stroke="currentColor" stroke-width="1.3"><rect x="1.5" y="3.5" width="13" height="9"/><path d="M1.5 3.5 8 9l6.5-5.5"/></svg>
          hello@mirapetal.com
        </li>
        <li>
          <svg viewBox="0 0 16 16" fill="currentColor"><path d="M3 2.5c1-.8 2-.6 2.5.3l1 1.8c.3.6.2 1.2-.4 1.6l-.8.5c.6 1.4 1.6 2.4 3 3l.5-.8c.4-.6 1-.7 1.6-.4l1.8 1c.9.5 1.1 1.5.3 2.5-.8 1-2 1.4-3.2 1C6 12 4 10 2.6 6.7 2 5.2 2.2 3.4 3 2.5z"/></svg>
          555-014-2287
        </li>
        <li>
          <svg viewBox="0 0 16 16" fill="none" stroke="currentColor" stroke-width="1.2"><circle cx="8" cy="8" r="6.5"/><ellipse cx="8" cy="8" rx="2.8" ry="6.5"/><path d="M1.5 8h13M2.6 4.6h10.8M2.6 11.4h10.8"/></svg>
          www.mirapetal.com
        </li>
      </ul>
    </div>
  </section>

  <section class="card card-front" aria-label="Business card front">
    <div class="name-band">
      <div class="front-name">Mira Petal</div>
      <div class="front-tagline">makeup artist</div>
    </div>
    <div class="front-contact front-email">hello@mirapetal.com</div>
    <div class="front-contact front-phone">555-014-2287</div>
    <div class="front-contact front-web">www.mirapetal.com</div>
  </section>

</body>
</html>
```